Make an Awesome Graphic for a PPT

Attached is the specific content for the project. the X-factor of Adoption. It does not need a title just take the existing graphic an improve it. Attached is our company logo for color palette and the "ugly version". It should look modern and edge in terms of effect and font. Need it by Monday March 7th

```html
<!DOCTYPE html>
<html lang="en">
<head>
<meta charset="utf-8">
<title>The X-Factor of Adoption</title>
<link href="https://fonts.googleapis.com/css2?family=Montserrat:wght@700;800&display=swap" rel="stylesheet">
<style>
  :root {
    --bg-light: #ffffff;
    --bg-mid: #dfe6ea;
    --bg-deep: #c2d2da;
    --arm-light: #f3f3f5;
    --arm-dark: #dedfe3;
    --arm-edge: #c9cbcf;
    --ring-light: #f6f6f7;
    --ring-dark: #d9dadd;
    --core-cyan: #0579c2;
    --core-indigo: #283a93;
    --label-blue: #1565b8;
    --label-white: #ffffff;
    --brand-blue: #1259ad;
  }
  html, body {
    margin: 0;
    padding: 0;
    width: 1200px;
    height: 691px;
    overflow: hidden;
  }
  .canvas {
    position: relative;
    width: 1200px;
    height: 691px;
    background:
      radial-gradient(ellipse 60% 55% at 100% 0%, var(--bg-light) 0%, rgba(255,255,255,0) 70%),
      linear-gradient(160deg, var(--bg-mid) 0%, #d3dee4 55%, var(--bg-deep) 100%);
    font-family: "Montserrat", sans-serif;
  }
  .adoption-diagram {
    position: absolute;
    left: 0;
    top: 0;
    width: 1200px;
    height: 691px;
  }
  .arm-label {
    font-family: "Montserrat", sans-serif;
    font-weight: 800;
    font-size: 21px;
    letter-spacing: 1.5px;
    fill: var(--label-blue);
  }
  .core-label {
    font-family: "Montserrat", sans-serif;
    font-weight: 700;
    font-size: 24px;
    letter-spacing: 0.5px;
    fill: var(--label-white);
  }
  .brand-name {
    position: absolute;
    right: 22px;
    bottom: 26px;
    margin: 0;
    font-family: "Montserrat", sans-serif;
    font-weight: 800;
    font-size: 46px;
    line-height: 1;
    letter-spacing: 1px;
    color: var(--brand-blue);
  }
</style>
</head>
<body>
<main class="canvas">
  <svg class="adoption-diagram" viewBox="0 0 1200 691" aria-label="The X-factor of adoption: farmer experience, farmer sentiment and innovation concept meeting in the adoption zone">
    <defs>
      <linearGradient id="arm-fill" x1="0" y1="0" x2="0" y2="1">
        <stop offset="0" stop-color="var(--arm-light)"/>
        <stop offset="1" stop-color="var(--arm-dark)"/>
      </linearGradient>
      <linearGradient id="ring-fill" x1="0" y1="0" x2="1" y2="1">
        <stop offset="0" stop-color="var(--ring-light)"/>
        <stop offset="1" stop-color="var(--ring-dark)"/>
      </linearGradient>
      <linearGradient id="core-fill" x1="0" y1="1" x2="1" y2="0">
        <stop offset="0.2" stop-color="var(--core-cyan)"/>
        <stop offset="0.85" stop-color="var(--core-indigo)"/>
      </linearGradient>
      <filter id="soft-shadow" x="-20%" y="-20%" width="140%" height="140%">
        <feDropShadow dx="4" dy="6" stdDeviation="6" flood-color="#6f8a99" flood-opacity="0.35"/>
      </filter>
    </defs>

    <!-- arm running top-left to bottom-right -->
    <g class="arm arm-descending" transform="translate(593 332) rotate(45)" filter="url(#soft-shadow)">
      <rect x="-296" y="-54" width="592" height="108" rx="54" fill="url(#arm-fill)" stroke="var(--arm-edge)" stroke-width="1.5"/>
    </g>
    <!-- arm running bottom-left to top-right -->
    <g class="arm arm-ascending" transform="translate(593 332) rotate(-45)" filter="url(#soft-shadow)">
      <rect x="-296" y="-54" width="592" height="108" rx="54" fill="url(#arm-fill)" stroke="var(--arm-edge)" stroke-width="1.5"/>
    </g>

    <!-- arm labels -->
    <g transform="translate(463 218) rotate(45)">
      <text class="arm-label" text-anchor="middle" y="-4">FARMER</text>
      <text class="arm-label" text-anchor="middle" y="20">EXPERIENCE</text>
    </g>
    <g transform="translate(722 198) rotate(-45)">
      <text class="arm-label" text-anchor="middle" y="-4">INNOVATION</text>
      <text class="arm-label" text-anchor="middle" y="20">CONCEPT</text>
    </g>
    <g transform="translate(468 453) rotate(-45)">
      <text class="arm-label" text-anchor="middle" y="-4">INNOVATION</text>
      <text class="arm-label" text-anchor="middle" y="20">CONCEPT</text>
    </g>
    <g transform="translate(726 466) rotate(45)">
      <text class="arm-label" text-anchor="middle" y="-4">FARMER</text>
      <text class="arm-label" text-anchor="middle" y="20">SENTIMENT</text>
    </g>

    <!-- adoption zone hub -->
    <g class="hub">
      <circle cx="593" cy="332" r="91" fill="url(#ring-fill)" filter="url(#soft-shadow)"/>
      <circle cx="593" cy="332" r="79" fill="var(--core-indigo)"/>
      <circle cx="594" cy="334" r="73" fill="url(#core-fill)"/>
      <text class="core-label" x="594" y="334" text-anchor="middle">ADOPTION</text>
      <text class="core-label" x="594" y="358" text-anchor="middle">ZONE</text>
    </g>
  </svg>

  <p class="brand-name">AGRIVANT</p>
</main>
</body>
</html>
```